Business card design needed

It's a new business in town.Something so the name stands out.I need a logo for the B.R.W
I may all so use the design as a sign on a building

Contact Information for Business Card

B.R.W
Brindlewood Auto Detailing
42 Fenwarra Crs
Brindlewood Vic 3799
Ph:(03)59284736
Mob:0417362958

```html
<!DOCTYPE html>
<html lang="en">
<head>
<meta charset="utf-8">
<title>B.R.W – Brindlewood Auto Detailing business card</title>
<link rel="stylesheet" href="https://fonts.googleapis.com/css2?family=Advent+Pro:wght@200;300&display=swap">
<style>
  :root {
    --stripe-1: #c84141;
    --stripe-2: #a53435;
    --stripe-3: #82292a;
    --stripe-4: #8e2a2b;
    --stripe-5: #b13b3b;
    --card-red: #b03a3b;
    --ink: #ffffff;
    --page: #ffffff;
  }
  html, body {
    margin: 0;
    padding: 0;
    width: 1003px;
    height: 1200px;
    overflow: hidden;
    background: var(--page);
  }
  .canvas {
    display: block;
    width: 1003px;
    height: 1200px;
  }
  .stripe-1 { fill: var(--stripe-1); }
  .stripe-2 { fill: var(--stripe-2); }
  .stripe-3 { fill: var(--stripe-3); }
  .stripe-4 { fill: var(--stripe-4); }
  .stripe-5 { fill: var(--stripe-5); }
  .inner-frame { fill: none; stroke: var(--ink); stroke-width: 5; }
  .emblem-circle { fill: var(--card-red); stroke: var(--ink); stroke-width: 7; }
  .emblem-rule { stroke: var(--ink); stroke-width: 2; }
  .back-panel { fill: var(--card-red); }
  .card-text {
    fill: var(--ink);
    font-family: "Advent Pro", sans-serif;
    font-weight: 300;
  }
  .brand-mark { font-size: 74px; font-weight: 200; letter-spacing: 2px; }
  .brand-tagline { font-size: 27px; }
  .back-mark { font-size: 43px; }
  .back-line { font-size: 34px; }
  .icon { fill: var(--ink); }
  .icon-outline { fill: none; stroke: var(--ink); stroke-width: 3; }
</style>
</head>
<body>
<svg class="canvas" viewBox="0 0 1003 1200" xmlns="http://www.w3.org/2000/svg">
  <!-- Front of card -->
  <g class="card-front" transform="translate(64 18)">
    <rect class="stripe-1" x="0" y="0" width="176" height="559"/>
    <rect class="stripe-2" x="175" y="0" width="176" height="559"/>
    <rect class="stripe-3" x="350" y="0" width="176" height="559"/>
    <rect class="stripe-4" x="525" y="0" width="176" height="559"/>
    <rect class="stripe-5" x="700" y="0" width="177" height="559"/>
    <rect class="inner-frame" x="12" y="13" width="853" height="531"/>
    <circle class="emblem-circle" cx="439" cy="278" r="247"/>
    <text class="card-text brand-mark" x="439" y="283" text-anchor="middle">B.R.W</text>
    <line class="emblem-rule" x1="294" y1="303" x2="585" y2="303"/>
    <text class="card-text brand-tagline" x="439" y="339" text-anchor="middle">Brindlewood Auto Detailing</text>
  </g>

  <!-- Back of card -->
  <g class="card-back" transform="translate(64 616)">
    <rect class="back-panel" x="0" y="0" width="877" height="400"/>
    <text class="card-text back-mark" x="439" y="97" text-anchor="middle">B.R.W</text>
    <text class="card-text back-line" x="439" y="142" text-anchor="middle">Brindlewood Auto Detailing</text>
    <text class="card-text back-line" x="439" y="195" text-anchor="middle">42 Fenwarra Crs Brindlewood Vic 3799</text>

    <g class="phone-icon" transform="translate(311 265)">
      <path class="icon" d="M0 8 Q22 -4 44 8 L42 16 L32 14 L30 9 Q22 6 14 9 L12 14 L2 16 Z"/>
      <path class="icon" d="M10 16 L34 16 L42 30 L2 30 Z"/>
    </g>
    <text class="card-text back-line" x="365" y="292">(03) 59284736</text>

    <g class="mobile-icon" transform="translate(325 307)">
      <rect class="icon-outline" x="1.5" y="1.5" width="21" height="37" rx="3"/>
      <line class="icon-outline" x1="2" y1="31" x2="22" y2="31"/>
    </g>
    <text class="card-text back-line" x="378" y="343">0417362958</text>
  </g>

  <!-- Stripe band below back -->
  <g class="stripe-band" transform="translate(64 1029)">
    <rect class="stripe-1" x="0" y="0" width="176" height="144"/>
    <rect class="stripe-2" x="175" y="0" width="176" height="144"/>
    <rect class="stripe-3" x="350" y="0" width="176" height="144"/>
    <rect class="stripe-4" x="525" y="0" width="176" height="144"/>
    <rect class="stripe-5" x="700" y="0" width="177" height="144"/>
  </g>
</svg>
</body>
</html>
```